Tiltwave Drinks, Packaging Design Project

We need an awesome package design for Tiltwave Drinks' initial product launch.

Our company was founded with the idea of creating an innovative alcoholic beverage product that caters to a previously under-served market of millenials aged 21-30 who love to have a good time. The product will be served in a box with a plastic bladder and a spigot.

**Although our product will be served in a box similar to Cordelle or Hanna Strom, we are NOT in the wine category. TiltWave will focus on spirit based beverages.

We've chosen a great logo to use as the foundation for our package design. We will attach a jpeg version for your reference. You do NOT need to stick to the colors that we have used for the logo - but your colors should be bold, fun, and inviting.

We're looking forward to seeing your work!

-K7
Updates

Hey All!

Thanks so much for your contributions so far!! We want to clarify a couple things as we move forward.  Our product will be a spirit-based alcoholic beverage in a box.  We Tiltwave is more reminiscent of "portable jungle juice" rather than repackaged table wine.  We'll be looking at designs that aim younger and and are a little more daring.  We hope this helps to clarify our goals.

We're also looking at differentiating through alternative package dimensions.  Though we want to stay with a 5 liter size, we would be interested in looking at dimensions that look more like a boombox (longer and shorter than a Cordelle box).   

One possible combination would be 30 cm wide x 18 cm high x 11 cm deep.  Though you do not to adhere to these dimensions, we hope it will help by providing you with further direction.

Thanks SO much and we're looking forward to working with you!

 - K7

Industry/Entity Type

Plastic

```html
<!DOCTYPE html>
<html lang="en">
<head>
<meta charset="utf-8">
<title>Tiltwave Drinks – Box Dieline</title>
<link rel="stylesheet" href="https://fonts.googleapis.com/css2?family=Josefin+Sans:wght@700&family=Cinzel+Decorative:wght@900&display=swap">
<style>
  :root {
    --paper: #ffffff;
    --cut-line: #c8c8c8;
    --ink: #141414;
    --flap-grey: #ececec;
    --ring-yellow: #ffd21a;
    --ring-orange: #f07a0c;
    --ring-deep: #b8360a;
    --ring-teal: #2fb3b0;
  }
  html, body {
    margin: 0;
    padding: 0;
    overflow: hidden;
    background: var(--paper);
  }
  .dieline {
    display: block;
    width: 1200px;
    height: 586px;
  }
  .brand-name {
    font-family: "Josefin Sans", sans-serif;
    font-weight: 700;
    fill: var(--ink);
    letter-spacing: 2px;
  }
  .flavour-name {
    font-family: "Cinzel Decorative", serif;
    font-weight: 900;
    fill: var(--ink);
  }
  .tagline {
    font-family: "Josefin Sans", sans-serif;
    font-weight: 700;
    font-size: 9px;
    letter-spacing: 1.6px;
    fill: var(--ink);
  }
  .fold-label {
    font-family: "Josefin Sans", sans-serif;
    font-size: 9px;
    fill: #888;
    letter-spacing: 1px;
  }
  .cut-line { stroke: var(--cut-line); stroke-width: 1; fill: none; }
</style>
</head>
<body>
<svg class="dieline" viewBox="0 0 1200 586" xmlns="http://www.w3.org/2000/svg">
  <defs>
    <radialGradient id="burst" cx="50%" cy="50%" r="50%">
      <stop offset="0%" stop-color="var(--ring-teal)"/>
      <stop offset="22%" stop-color="var(--ring-deep)"/>
      <stop offset="55%" stop-color="var(--ring-orange)"/>
      <stop offset="82%" stop-color="var(--ring-yellow)"/>
      <stop offset="100%" stop-color="var(--ring-yellow)" stop-opacity="0"/>
    </radialGradient>
    <radialGradient id="flap-haze" cx="50%" cy="60%" r="60%">
      <stop offset="0%" stop-color="var(--flap-grey)"/>
      <stop offset="100%" stop-color="var(--paper)"/>
    </radialGradient>
    <linearGradient id="bottom-fade" x1="0" y1="0" x2="0" y2="1">
      <stop offset="0%" stop-color="var(--ring-yellow)" stop-opacity="0.45"/>
      <stop offset="100%" stop-color="var(--paper)" stop-opacity="0"/>
    </linearGradient>
  </defs>

  <!-- top flap -->
  <g class="top-flap">
    <rect x="600" y="0" width="438" height="156" fill="url(#flap-haze)" role="img" aria-label="Faint grey concentric ring pattern"/>
    <ellipse cx="820" cy="70" rx="95" ry="62" fill="url(#burst)" opacity="0.8" role="img" aria-label="Orange and yellow radiating ring burst"/>
    <text class="flavour-name" x="820" y="90" font-size="52" text-anchor="middle">TILT</text>
    <text class="tagline" x="820" y="154" text-anchor="middle">FOR THE TILTWAVE HIGH SPIRIT SEEKER!</text>
  </g>

  <!-- bottom flap -->
  <rect class="bottom-flap" x="600" y="426" width="438" height="160" fill="url(#bottom-fade)" role="img" aria-label="Fading yellow ring pattern"/>

  <!-- left front panel -->
  <g class="panel panel-left">
    <ellipse cx="216" cy="288" rx="215" ry="142" fill="url(#burst)" role="img" aria-label="Orange and yellow concentric ring burst with teal star"/>
    <text class="brand-name" x="216" y="300" font-size="40" text-anchor="middle">TILTWAVE DRINKS</text>
  </g>

  <!-- left side panel -->
  <g class="panel panel-side-left">
    <ellipse cx="530" cy="288" rx="84" ry="132" fill="url(#burst)" role="img" aria-label="Orange and yellow ring burst with teal spiral"/>
    <text class="flavour-name" font-size="48" text-anchor="middle" transform="translate(548 288) rotate(90)">TILT</text>
  </g>

  <!-- centre front panel -->
  <g class="panel panel-front">
    <ellipse cx="820" cy="300" rx="222" ry="178" fill="url(#burst)" role="img" aria-label="Orange and yellow concentric ring burst with teal star"/>
    <text class="brand-name" x="820" y="302" font-size="40" text-anchor="middle">TILTWAVE DRINKS</text>
  </g>

  <!-- right side panel -->
  <g class="panel panel-side-right">
    <ellipse cx="1116" cy="288" rx="78" ry="128" fill="url(#burst)" role="img" aria-label="Orange and yellow ring burst with teal spiral"/>
    <text class="flavour-name" font-size="48" text-anchor="middle" transform="translate(1134 288) rotate(90)">TILT</text>
  </g>

  <!-- cut and fold lines -->
  <g class="cut-lines">
    <path class="cut-line" d="M0 156 H600 V0 M1038 0 V156 H1200"/>
    <path class="cut-line" d="M0 426 H600 V586 M1038 586 V426 H1200"/>
    <line class="cut-line" x1="441" y1="108" x2="441" y2="474"/>
  </g>
  <text class="fold-label" transform="translate(432 146) rotate(-90)">FOLD</text>
</svg>
</body>
</html>
```